Need simple and modern looking business card with all my information on one side and logo on the other side
Info :
Company name - VELMAR CONSTRUCTION LLC
Company addres- 418 harbor 87th. Dunmoor park ny 10352
Email- velmarllc@tridomail.Com
Company phone number 555-318-6094
Cell number- 555-742-0583
Web site - velmarllc.Com
My name Gerald tomasino

Target Market(s)

Construction , home improvement, remodeling

Industry/Entity Type

Construction

Contact Information for Business Card

It has to be moder but at the same time simple

Font styles to use
Sans Serif

Colors
0255a3
ffffff
000000
f78f20
b1b1b1
9d9d9d
1b1b1b
33a6d7
ec1f27

Requirements
Must have
• My logo on one side maybe with a some kind of background on the other side all my information
Nice to have
• Some kind of background pictures provided by you .PLEASE HAVE ACCOUNT WITH PIXELVAULT WILL NOT PAY ANY EXTRA FEES .
Should not have
• Any kind of hamer, nails,screws, helmets itp. Please do not copy the other designs come up with something new.

```html
<!DOCTYPE html>
<html lang="en">
<head>
<meta charset="utf-8">
<title>Velmar Construction LLC – Business Card</title>
<link href="https://fonts.googleapis.com/css2?family=Open+Sans:wght@400;600;700&display=swap" rel="stylesheet">
<style>
  :root {
    --orange: #f78f20;
    --orange-soft: #f9b060;
    --black: #000000;
    --ink: #1b1b1b;
    --grey-light: #b1b1b1;
    --white: #ffffff;
    --stage: #e6e4e1;
  }
  * { box-sizing: border-box; margin: 0; padding: 0; }
  html, body {
    width: 1200px; height: 906px; overflow: hidden;
    background: var(--stage);
    font-family: "Open Sans", Arial, sans-serif;
  }
  .canvas { position: relative; width: 1200px; height: 906px; }
  .card {
    position: absolute; width: 700px; height: 400px;
    background: var(--white); border-radius: 18px; overflow: hidden;
    box-shadow: 0 6px 18px rgba(0,0,0,0.18);
  }
  .card--front { left: 60px; top: 40px; }
  .card--back { left: 440px; top: 466px; }

  .wordmark { position: absolute; display: flex; align-items: center; gap: 14px; color: var(--ink); font-weight: 700; }
  .wordmark__square { background: var(--orange); flex: none; }
  .wordmark__text { line-height: 1.05; }
  .wordmark__name { display: block; letter-spacing: 2px; }
  .wordmark__sub { display: block; letter-spacing: 1px; }

  .card--front .wordmark { left: 50%; top: 50%; transform: translate(-50%, -50%); }
  .card--front .wordmark__square { width: 34px; height: 34px; }
  .card--front .wordmark__name { font-size: 62px; }
  .card--front .wordmark__sub { font-size: 24px; }

  .header-band {
    position: absolute; left: 0; top: 0; width: 700px; height: 130px;
    background: linear-gradient(90deg, var(--orange) 0%, var(--orange-soft) 50%, var(--orange) 80%);
  }

  .address {
    position: absolute; right: 26px; top: 26px; text-align: right;
    color: var(--white); font-size: 15px; line-height: 1.35;
  }

  .contacts { position: absolute; right: 22px; top: 190px; list-style: none; }
  .contacts li {
    display: flex; justify-content: flex-end; align-items: center; gap: 12px;
    font-size: 16px; color: var(--black); height: 34px;
  }
  .contacts svg { width: 18px; height: 18px; flex: none; }

  .card--back .wordmark { left: 36px; top: 262px; gap: 10px; }
  .card--back .wordmark__square { width: 22px; height: 22px; }
  .card--back .wordmark__name { font-size: 34px; }
  .card--back .wordmark__sub { font-size: 13px; }

  .holder-name {
    position: absolute; left: 36px; bottom: 26px;
    color: var(--orange); font-weight: 700; font-size: 22px;
  }
</style>
</head>
<body>
<main class="canvas">

  <section class="card card--front" aria-label="Business card front">
    <div class="wordmark">
      <span class="wordmark__square"></span>
      <span class="wordmark__text">
        <span class="wordmark__name">VELMAR</span>
        <span class="wordmark__sub">CONSTRUCTION LLC</span>
      </span>
    </div>
  </section>

  <section class="card card--back" aria-label="Business card back">
    <div class="header-band" role="img" aria-label="Decorative orange band with white, grey and black accent stripes"></div>

    <p class="address">418 harbor 87th.<br>Dunmoor park ny 10352</p>

    <ul class="contacts">
      <li>555-318-6094
        <svg viewBox="0 0 20 20" aria-hidden="true"><circle cx="10" cy="10" r="8.5" fill="none" stroke="#f78f20" stroke-width="1.5"/><path d="M7 5.5 L8.5 8 L7.5 9 Q8.5 11.5 11 12.5 L12 11.5 L14.5 13 L13.5 14.5 Q8 14 5.5 7 Z" fill="#f78f20"/></svg>
      </li>
      <li>555-742-0583
        <svg viewBox="0 0 20 20" aria-hidden="true"><rect x="6" y="2.5" width="8" height="15" rx="1.5" fill="none" stroke="#f78f20" stroke-width="1.5"/><circle cx="10" cy="15" r="0.9" fill="#f78f20"/></svg>
      </li>
      <li>velmarllc@tridomail.Com
        <svg viewBox="0 0 20 20" aria-hidden="true"><rect x="2" y="5" width="16" height="11" fill="none" stroke="#f78f20" stroke-width="1.5"/><path d="M2 5 L10 11 L18 5" fill="none" stroke="#f78f20" stroke-width="1.5"/></svg>
      </li>
      <li>www.velmarllc.Com
        <svg viewBox="0 0 20 20" aria-hidden="true"><circle cx="10" cy="10" r="8" fill="none" stroke="#f78f20" stroke-width="1.5"/><ellipse cx="10" cy="10" rx="3.5" ry="8" fill="none" stroke="#f78f20" stroke-width="1.2"/><path d="M2 10 H18 M3.5 6 H16.5 M3.5 14 H16.5" stroke="#f78f20" stroke-width="1.2"/></svg>
      </li>
    </ul>

    <div class="wordmark">
      <span class="wordmark__square"></span>
      <span class="wordmark__text">
        <span class="wordmark__name">VELMAR</span>
        <span class="wordmark__sub">CONSTRUCTION LLC</span>
      </span>
    </div>

    <p class="holder-name">Gerald Tomasino</p>
  </section>

</main>
</body>
</html>
```